Quillo Stake Pool, redesign of existing website

Quillo is a stake pool that allow its users to stake their Tarnex crypto to yearn stable yields. The existing site is at www.quillostake.org The site is today is a little dull and I want to have suggestions for a redesign that makes the site stand out and that picks up the colors of the logo. I am not looking for a complete redesign, mainly colors and smaller changes to layout. Examples of sites to be inspired by www.vemba.network, https://app.toradel.finance/

Target Market(s)

Crypto users on Tarnex

Number of Pages Required

1 page

```html
<!DOCTYPE html>
<html lang="en">
<head>
<meta charset="utf-8">
<title>Quillo Stake – Liquid Staking on Tarnex</title>
<link rel="stylesheet" href="https://fonts.googleapis.com/css2?family=Alegreya:wght@700&family=Poppins:wght@400;500;600&display=swap">
<style>
:root{
  --bg-header:#121a2c;
  --bg-main:#162036;
  --bg-deep:#121a2b;
  --bg-panel:#111827;
  --bg-card:#1c2744;
  --bg-button:#1f2b4b;
  --teal:#16a0ad;
  --orange:#f47321;
  --white:#ffffff;
  --muted:#dfe4ee;
  --line:#2b3650;
}
*{box-sizing:border-box;margin:0;padding:0}
html,body{width:1200px;height:3122px;overflow:hidden}
body{position:relative;background:var(--bg-main);font-family:'Poppins',sans-serif;color:var(--white)}
.abs{position:absolute}
.band{position:absolute;left:0;width:1200px}
.header{top:0;height:113px;background:var(--bg-header)}
.brand{display:flex;align-items:center;gap:14px;font-weight:600;font-size:28px;color:var(--white)}
.brand .dot{width:52px;height:52px;border-radius:50%;background:var(--teal)}
.nav a{position:absolute;font-size:14px;color:var(--white);text-decoration:none;white-space:nowrap}
.nav a.active{color:var(--teal)}
.btn-dark{position:absolute;background:var(--bg-button);color:var(--teal);border-radius:8px;display:flex;align-items:center;justify-content:center;font-size:14px;text-transform:uppercase}
.serif{font-family:'Alegreya',serif;font-weight:700;color:var(--teal)}
.hero-title{top:190px;width:1200px;text-align:center;font-size:62px}
.lead{width:1200px;text-align:center;font-size:14px;line-height:22px}
.panel{left:76px;top:538px;width:1050px;height:518px;background:var(--bg-panel);border-radius:10px}
.tab{position:absolute;top:622px;width:264px;height:59px;border-radius:8px;display:flex;align-items:center;justify-content:center;font-size:17px;font-weight:500;text-transform:uppercase}
.tab.on{background:var(--orange);color:var(--white)}
.tab.off{border:1px solid var(--orange);color:var(--orange)}
.apy{left:187px;top:700px;font-size:26px;font-weight:500}
.field{position:absolute;top:795px;width:403px;height:56px;background:var(--white);border-radius:8px;color:#111;display:flex;justify-content:space-between;align-items:center;padding:0 18px 0 48px;font-size:25px;font-weight:500}
.meta{position:absolute;top:858px;font-size:12.5px;white-space:nowrap}
.meta u{text-underline-offset:2px}
.cta{left:468px;top:916px;width:263px;height:59px;background:var(--teal);border-radius:8px;display:flex;align-items:center;justify-content:center;font-size:18px;font-weight:500}
.defi-title{left:228px;top:1115px;font-size:48px}
.defi-text{left:228px;top:1194px;width:418px;font-size:13.3px;line-height:27px;text-align:justify}
.pill{position:absolute;left:736px;width:235px;height:52px;background:var(--bg-button);border-radius:8px;display:flex;align-items:center;justify-content:center;font-size:18px;font-weight:500}
.validators{top:1404px;height:716px;background:var(--bg-deep)}
.val-title{top:1478px;width:1200px;text-align:center;font-size:48px}
.val-text{left:156px;top:1558px;width:888px;text-align:center;font-size:13.5px;line-height:27px}
.card{position:absolute;top:1704px;width:214px;height:312px;background:var(--bg-card);border-radius:12px;text-align:center;padding:0 14px}
.card .ring{width:82px;height:82px;border-radius:50%;border:2px solid var(--teal);margin:30px auto 0;display:flex;align-items:center;justify-content:center}
.card .ring span{width:68px;height:68px;border-radius:50%;background:var(--teal);display:block}
.card h3{font-size:16px;font-weight:600;margin-top:12px;line-height:21px}
.card p{font-size:10px;line-height:17.4px;margin-top:10px;letter-spacing:-0.1px}
.card a{position:absolute;left:0;right:0;bottom:30px;font-size:11px;color:var(--teal);font-weight:600;text-decoration:underline}
.slider{top:2120px;height:640px;background:var(--bg-main)}
.vcard{left:269px;top:2180px;width:662px;height:481px;background:var(--bg-panel);border-radius:12px}
.arrow{position:absolute;top:2399px;width:48px;height:48px;border-radius:50%;display:flex;align-items:center;justify-content:center}
.arrow.prev{left:189px;background:var(--bg-button)}
.arrow.next{left:963px;background:var(--bg-panel)}
.lbl{position:absolute;left:343px;color:var(--teal);font-size:19px}
.val{position:absolute;font-size:20px;color:var(--muted);white-space:nowrap}
.small{position:absolute;left:442px;font-size:12.5px;color:var(--muted);white-space:nowrap}
.footer{top:2760px;height:362px;background:var(--bg-deep)}
.foot-rule{left:76px;top:2964px;width:1050px;height:1px;background:var(--line)}
.foot-nav a{position:absolute;top:3003px;font-size:16px;color:var(--white);text-decoration:none}
.bottom{top:3060px;height:62px;background:#10172a}
.copy{left:76px;top:3083px;font-size:12.5px}
.social{position:absolute;top:3078px;width:30px;height:30px;border:1px solid var(--white);border-radius:4px}
</style>
</head>
<body>

<header class="band header"></header>
<div class="abs brand" style="left:76px;top:31px"><span class="dot"></span>Quillo Stake</div>
<nav class="nav">
  <a class="active" style="left:558px;top:47px">Home</a>
  <a style="left:628px;top:47px">Liquid Staking</a>
  <a style="left:750px;top:47px">Validators</a>
  <a style="left:847px;top:47px">Docs</a>
  <a style="left:909px;top:47px">More ▾</a>
</nav>
<div class="btn-dark" style="left:991px;top:37px;width:135px;height:39px;font-size:13px">Select Wallet</div>

<h1 class="abs serif hero-title">Liquid Staking on Tarnex</h1>
<p class="abs lead" style="top:292px">Quillo Stake Pool offers non-custodial staking. Stake your TNX to receive a liquid staking token, quilloTNX, that you can use in Defi on Tarnex.</p>
<p class="abs lead" style="top:335px;left:110px;width:980px">Let us take care of managing your stake across the best validators on Tarnex, and your staking rewards will be automatically compounded each epoch. The value of quilloTNX relative to TNX will increase every epoch.</p>
<div class="btn-dark" style="left:512px;top:425px;width:176px;height:53px;font-size:15px">Know More</div>

<section class="abs panel"></section>
<div class="tab on" style="left:187px">Stake</div>
<div class="tab off" style="left:468px">Unstake</div>
<div class="tab off" style="left:749px">Referral</div>
<div class="abs apy">Current APY: 8.03% across 60 validators</div>
<div class="field" style="left:187px"><span>TNX</span><span>0</span></div>
<div class="field" style="left:610px"><span>quilloTNX</span><span>0</span></div>
<div class="meta" style="left:187px">balance: 0 TNX</div>
<div class="meta" style="left:534px"><u>max half</u></div>
<div class="meta" style="left:610px">balance: 0 quilloTNX</div>
<div class="meta" style="left:866px"><u>1 quilloTNX ≈ 1.01714 TNX</u></div>
<div class="abs cta">CONNECT WALLET</div>

<h2 class="abs serif defi-title">Defi Integrations</h2>
<p class="abs defi-text">The quillo liquid staking token, quilloTNX, can be used on the following Defi applications. We are constantly evaluating new integrations, so if you are missing an integration that you would like to see, please let us know!</p>
<div class="pill" style="top:1138px">Liquidity</div>
<div class="pill" style="top:1200px">Borrow &amp; Lending</div>
<div class="pill" style="top:1262px">Other</div>

<section class="band validators"></section>
<h2 class="abs serif val-title">Validators</h2>
<p class="abs val-text">Here you can find all active validators and their corresponding Quillo Rank and Quillo Score. The top ranked Validators will receive stake from the Quillo Stake Pool. For more information about how we rank validators, please have a look at the documentation. The Quillo Score (and rank) is calculated using the last completed epoch (589).</p>

<article class="card" style="left:128px"><div class="ring"><span role="img" aria-label="Calculator icon"></span></div><h3>As a validator how<br>do I get a delegation?</h3><p>Join the #validators channel on our Chatterly, this is a great place to ask questions directly to us and get help from fellow validators</p><a>READ MORE</a></article>
<article class="card" style="left:373px"><div class="ring"><span role="img" aria-label="Delegation chart icon"></span></div><h3>Delegation Strategy</h3><p>Our deep belief is that in order to be a good staking pool, we must deliver both for our users AND the network (which ultimately is good for every-one of course).</p><a>READ MORE</a></article>
<article class="card" style="left:616px"><div class="ring"><span role="img" aria-label="Governance building icon"></span></div><h3>Governance</h3><p>Any proposed changes to the delegation strategy will be posted at least 10 epochs in advance in the #governance channel on the Quillo Stake</p><a>READ MORE</a></article>
<article class="card" style="left:859px"><div class="ring"><span role="img" aria-label="Token coins icon"></span></div><h3>The QLO token</h3><p>We plan to release a governance token, QLO, in the near future. Target date is during Q2 2024. The QLO token will be used to steer gover-nance of the Quillo Stake</p><a>READ MORE</a></article>

<section class="band slider"></section>
<div class="abs vcard"></div>
<div class="arrow prev"><svg width="20" height="14" viewBox="0 0 20 14"><path d="M19 7H2M7 1L1 7l6 6" stroke="#fff" stroke-width="2.4" fill="none"/></svg></div>
<div class="arrow next"><svg width="20" height="14" viewBox="0 0 20 14"><path d="M1 7h17M13 1l6 6-6 6" stroke="#fff" stroke-width="2.4" fill="none"/></svg></div>
<div class="lbl" style="top:2239px">Rank:</div><div class="val" style="left:442px;top:2234px;font-size:24px">1</div>
<div class="lbl" style="top:2287px">Name:</div><div class="val" style="left:442px;top:2284px;font-size:23px">Bramblecrest Ventures</div>
<div class="small" style="top:2316px">Identity:&nbsp;&nbsp; KP4WQMRVZTLFxhjqrdm7n5eg2QkvbWTp8stLHNcrBRQA</div>
<div class="small" style="top:2339px">Vote:&nbsp;&nbsp; rTBNwKa8j5hQ2LtvcpF6dXmnBb3sRoazmT4kgDyHpU</div>
<div class="lbl" style="top:2374px">Active Stake:</div><div class="val" style="left:494px;top:2372px;font-size:22px">313.4 kTNX</div>
<div class="lbl" style="top:2410px">Quillo Stake:</div><div class="val" style="left:494px;top:2410px;font-size:18px">Current:&nbsp;&nbsp; 0.008 TNX</div>
<div class="val" style="left:494px;top:2442px;font-size:18px">Target:&nbsp;&nbsp; 19.887 TNX</div>
<div class="lbl" style="top:2480px">Comm %:</div><div class="val" style="left:494px;top:2480px;font-size:18px">0%</div>
<div class="lbl" style="top:2511px">APY %:</div><div class="val" style="left:494px;top:2511px;font-size:18px">0%</div>
<div class="lbl" style="top:2553px">Quillo Score:</div><div class="val" style="left:494px;top:2553px;font-size:18px">0.99824</div>
<div class="val" style="left:494px;top:2584px;font-size:18px">V&nbsp;&nbsp;&nbsp;&nbsp;&nbsp;&nbsp;&nbsp; S1&nbsp;&nbsp;&nbsp;&nbsp;&nbsp;&nbsp; S2</div>

<footer class="band footer"></footer>
<div class="abs brand" style="left:481px;top:2850px"><span class="dot"></span>Quillo Stake</div>
<div class="abs foot-rule"></div>
<nav class="foot-nav">
  <a style="left:301px">HOME</a>
  <a style="left:409px">LIQUID STAKING</a>
  <a style="left:590px">VALIDATORS</a>
  <a style="left:746px">DOCS</a>
  <a style="left:855px">MORE</a>
</nav>
<div class="band bottom"></div>
<div class="abs copy">Copyright © 2024 All Rights Reserved By Quillo Stake</div>
<span class="social" style="left:988px"></span>
<span class="social" style="left:1023px"></span>
<span class="social" style="left:1058px"></span>
<span class="social" style="left:1094px"></span>

</body>
</html>
```